International service dog training school needs web design

We need to upgrade our website. The website is https://brightpathmentor.site/
We help trainers and service dog programs learn how to train service dogs with the latest and most ethical training methods. We offer online and in-person coaching services. We would like to see designs that are engaging and communicate professionalism, expertise, and care for the dogs and people we work with. Please also keep the colors already in the logo in the design.

```html
<!DOCTYPE html>
<html lang="en">
<head>
<meta charset="utf-8">
<title>Bright Path Mentor – Assistance Canines</title>
<link rel="stylesheet" href="https://fonts.googleapis.com/css2?family=Rubik:wght@400;500&family=Roboto:wght@400;500;700&display=swap">
<style>
:root{
  --blue:#2172c0;
  --blue-dark:#1a5fa6;
  --teal:#05a79f;
  --teal-dark:#038c85;
  --ink:#1d1d1f;
  --text:#6b6b6b;
  --footer:#262626;
  --white:#ffffff;
}
*{margin:0;padding:0;box-sizing:border-box}
html,body{width:1200px;height:5072px;overflow:hidden}
body{position:relative;background:var(--white);font-family:"Roboto",Arial,sans-serif;color:var(--text)}
.abs{position:absolute}
.heading{font-family:"Rubik","Roboto",sans-serif;font-weight:400;text-transform:uppercase;letter-spacing:.5px}
.btn{position:absolute;display:flex;align-items:center;justify-content:center;gap:8px;border-radius:24px;color:#fff;font-weight:700;font-size:14px;text-transform:uppercase;white-space:nowrap}
.btn .arrow{width:14px;height:14px}
.btn-teal{background:var(--teal)}
.btn-blue{background:var(--blue)}
.photo{position:absolute}

/* header */
.site-header{position:absolute;left:0;top:0;width:1200px;height:85px;background:#fff;border-top:4px solid var(--blue)}
.brand{position:absolute;left:112px;top:28px;display:flex;align-items:center;gap:10px;color:var(--teal);font-weight:500;font-size:18px}
.brand-dot{width:26px;height:26px;border-radius:50%;background:var(--teal)}
.nav{position:absolute;left:378px;top:32px;display:flex;gap:27px;font-size:14px;font-weight:500;color:#222}
.login{position:absolute;left:988px;top:24px;width:100px;height:38px;background:var(--teal);border-radius:20px;color:#fff;font-weight:500;font-size:15px;display:flex;align-items:center;justify-content:center;gap:6px}

/* hero */
.hero-title{left:110px;top:222px;color:#fff;font-size:40px;line-height:48px}
.hero-text{left:110px;top:338px;width:480px;color:#fff;font-size:15px;line-height:27px}
.service{position:absolute;width:300px;height:300px;border-radius:50%;border:6px solid #fff;color:#fff;text-align:center;padding:50px 34px 0}
.service svg{width:50px;height:50px}
.service h3{font-size:18px;font-weight:700;margin:8px 0 14px;line-height:20px}
.service p{font-size:13px;line-height:22px}
.service .more{margin-top:18px;font-size:14px;font-weight:700;display:flex;align-items:center;justify-content:center;gap:7px}

/* who */
.who-title{left:600px;top:990px;font-size:40px;color:var(--ink)}
.who-text{left:600px;top:1058px;width:490px;font-size:13.5px;line-height:27px}
.who-text p+p{margin-top:10px}

/* courses */
.courses-title{left:0;width:1200px;top:1544px;text-align:center;color:#fff;font-size:40px}
.course{position:absolute;width:308px;background:#fff;border-radius:6px;box-shadow:0 6px 18px rgba(0,0,0,.15);padding:6px 6px 0;text-align:center}
.course .pic{height:216px;border-radius:3px}
.course .icon{width:62px;height:62px;border-radius:50%;background:var(--blue);border:4px solid #fff;margin:-34px auto 0;position:relative;display:flex;align-items:center;justify-content:center}
.course h4{font-size:16px;font-weight:500;color:#111;margin:12px 0 10px}
.course p{font-size:13px;line-height:22px;padding:0 14px}
.course .btn{position:relative;margin:20px auto 0;width:146px;height:42px}

/* features */
.section-title{left:0;width:1200px;text-align:center;font-size:40px;color:var(--ink)}
.feature-box{position:absolute;color:#fff}
.feature-box h3{font-family:"Rubik",sans-serif;font-weight:400;font-size:33px;line-height:42px;text-transform:uppercase}
.feature-box p{font-size:13.5px;line-height:23px;margin-top:14px}
.round-icon{position:absolute;width:76px;height:76px;border-radius:50%;border:4px solid #fff;display:flex;align-items:center;justify-content:center}

/* book */
.book-title{left:110px;top:3456px;color:#fff;font-size:36px;line-height:46px}
.book-text{left:110px;top:3572px;width:500px;color:#fff;font-size:16px;line-height:27px;font-weight:500}

/* blog */
.post-main{position:absolute;left:138px;top:4019px;width:449px;height:453px;background:#fff;box-shadow:0 4px 16px rgba(0,0,0,.12);padding:12px;text-align:center}
.post-main .pic{height:292px}
.post-main h4{font-size:16px;font-weight:700;color:#222;margin-top:14px}
.meta{font-size:13px;color:var(--teal);margin-top:8px}
.post-main p{font-size:13px;line-height:21px;margin-top:12px;padding:0 30px}
.post-small{position:absolute;left:613px;width:447px;height:128px;background:#fff;box-shadow:0 4px 16px rgba(0,0,0,.12);padding:10px}
.post-small .pic{position:absolute;left:10px;top:10px;width:155px;height:108px}
.post-small .body{position:absolute;left:182px;top:14px;width:250px}
.post-small h5{font-size:14px;font-weight:700;color:#222}
.post-small .meta{font-size:12.5px;margin-top:6px}
.post-small p{font-size:13px;line-height:20px;margin-top:8px}

/* footer */
.foot-h{position:absolute;color:#fff;font-weight:700;font-size:15px;text-transform:uppercase}
.field{position:absolute;background:#fff;font-size:11px;color:#777;padding:10px 14px;height:38px}
.quick{position:absolute;left:640px;top:4750px;list-style:none;color:#fff;font-size:13.5px}
.quick li{height:30px;display:flex;align-items:center;gap:12px}
.contact{position:absolute;left:851px;top:4750px;color:#fff;font-size:13.5px;line-height:22px;list-style:none}
.contact li{display:flex;gap:14px;margin-bottom:13px}
.contact svg{flex:0 0 14px;width:14px;height:14px;margin-top:4px}
.social{position:absolute;top:4908px;width:32px;height:32px;border-radius:50%;background:#fff}
.copyright{position:absolute;left:0;width:1200px;top:5032px;text-align:center;color:#fff;font-size:13px}
</style>
</head>
<body>

<!-- header -->
<header class="site-header">
  <div class="brand"><span class="brand-dot"></span>Bright Path Mentor</div>
  <nav class="nav"><span>The Center</span><span>Helping organizations</span><span>Teaching Trainers</span><span>Research</span><span>Contact</span></nav>
  <div class="login"><svg width="12" height="13" viewBox="0 0 12 13"><rect x="1" y="6" width="10" height="7" rx="1" fill="#fff"/><path d="M3 6V4a3 3 0 0 1 6 0v2" stroke="#fff" stroke-width="1.8" fill="none"/></svg>Login</div>
</header>

<!-- hero -->
<div class="photo" role="img" aria-label="Golden retriever sitting on a sunny lawn" style="left:0;top:85px;width:1200px;height:640px;background:linear-gradient(100deg,#5e7a34 0%,#7c9440 40%,#b8b07a 65%,#d9cfb4 78%,#8aa048 100%)"></div>
<svg class="abs" style="left:0;top:560px" width="1200" height="180" viewBox="0 0 1200 180"><path d="M0 150 Q 520 20 1200 110 L1200 180 L0 180 Z" fill="#fff"/></svg>
<h1 class="abs heading hero-title">Medical Assistance<br>Canines</h1>
<p class="abs hero-text">The Bright Path Center for Assistance Canines was founded by Helena Marsh Ph.D.</p>
<div class="btn btn-teal" style="left:110px;top:420px;width:192px;height:50px">Get Started <svg class="arrow" viewBox="0 0 14 14"><circle cx="7" cy="7" r="7" fill="#fff"/><path d="M5.5 4l3 3-3 3" stroke="var(--teal)" stroke-width="2" fill="none"/></svg></div>

<div class="service" style="left:167px;top:589px;background:var(--blue)">
  <svg viewBox="0 0 50 50" fill="none" stroke="#fff" stroke-width="2"><circle cx="25" cy="12" r="6"/><path d="M14 30c0-6 5-10 11-10s11 4 11 10"/><rect x="8" y="30" width="34" height="5"/><path d="M12 35v10M38 35v10"/></svg>
  <h3>Program Consulting</h3>
  <p>Helping organizations get started, improve their training program, and add services</p>
  <div class="more">Learn More <svg class="arrow" width="14" height="14" viewBox="0 0 14 14"><circle cx="7" cy="7" r="7" fill="#fff"/><path d="M5.5 4l3 3-3 3" stroke="var(--blue)" stroke-width="2" fill="none"/></svg></div>
</div>
<div class="service" style="left:449px;top:589px;background:var(--teal)">
  <svg viewBox="0 0 50 50" fill="none" stroke="#fff" stroke-width="2"><rect x="7" y="6" width="36" height="22" rx="2"/><circle cx="14" cy="38" r="4"/><circle cx="25" cy="38" r="4"/><circle cx="36" cy="38" r="4"/><path d="M8 48c0-3 3-5 6-5s6 2 6 5M19 48c0-3 3-5 6-5s6 2 6 5M30 48c0-3 3-5 6-5s6 2 6 5"/></svg>
  <h3>Seminar/Presentations</h3>
  <p>We can give in person or online seminars on service dog training and medical detection dogs.</p>
  <div class="more">Learn More <svg class="arrow" width="14" height="14" viewBox="0 0 14 14"><circle cx="7" cy="7" r="7" fill="#fff"/><path d="M5.5 4l3 3-3 3" stroke="var(--teal)" stroke-width="2" fill="none"/></svg></div>
</div>
<div class="service" style="left:731px;top:589px;background:var(--blue)">
  <svg viewBox="0 0 50 50" fill="none" stroke="#fff" stroke-width="2"><circle cx="25" cy="16" r="8"/><path d="M10 46c0-9 7-15 15-15s15 6 15 15"/><path d="M25 2v4M39 16h4M7 16h4"/></svg>
  <h3>Online or in person consulting</h3>
  <p>Consulting services for your service dog organization.</p>
  <div class="more">Learn More <svg class="arrow" width="14" height="14" viewBox="0 0 14 14"><circle cx="7" cy="7" r="7" fill="#fff"/><path d="M5.5 4l3 3-3 3" stroke="var(--blue)" stroke-width="2" fill="none"/></svg></div>
</div>

<!-- who we are -->
<div class="photo" role="img" aria-label="Trainers and dogs at a group training session" style="left:112px;top:978px;width:404px;height:404px;border-radius:50%;background:radial-gradient(circle at 50% 40%,#a49a8c 0%,#6d6760 55%,#3f4b5c 100%)"></div>
<h2 class="abs heading who-title">Who We Are</h2>
<div class="abs who-text">
  <p>The Bright Path Center for Assistance Canines was founded by Helena Marsh Ph.D. in response to demand for coaching from dog trainers, medical professionals, and service dog programs.</p>
  <p>Helena Marsh Ph.D. has helped hundreds of trainers and several programs both in the US and internationally, expand the type of dogs they could offer to include medical alert dogs. Specialized mostly in the training of diabetic alert dogs, seizure dogs.</p>
</div>
<div class="btn btn-teal" style="left:600px;top:1288px;width:162px;height:44px">Read More <svg class="arrow" viewBox="0 0 14 14"><circle cx="7" cy="7" r="7" fill="#fff"/><path d="M5.5 4l3 3-3 3" stroke="var(--teal)" stroke-width="2" fill="none"/></svg></div>

<!-- courses -->
<svg class="abs" style="left:0;top:1458px" width="1200" height="770" viewBox="0 0 1200 770"><defs><linearGradient id="courseBand" x1="0" x2="0" y1="0" y2="1"><stop offset="0" stop-color="#2a7ccb"/><stop offset="1" stop-color="#1c66b2"/></linearGradient></defs><path d="M0 120 Q 600 -60 1200 120 L1200 650 Q 600 860 0 650 Z" fill="url(#courseBand)"/></svg>
<h2 class="abs heading courses-title">Our Courses</h2>

<div class="course" style="left:112px;top:1625px;height:460px">
  <div class="pic" role="img" aria-label="Trainers walking service dogs in a hallway" style="background:linear-gradient(160deg,#c9c5bf,#7d6f63 60%,#4c4540)"></div>
  <div class="icon"><svg width="30" height="30" viewBox="0 0 30 30" fill="none" stroke="#fff" stroke-width="2"><path d="M8 8l-3 6 4 2M22 8l3 6-4 2"/><circle cx="15" cy="16" r="8"/><circle cx="12" cy="15" r="1" fill="#fff"/><circle cx="18" cy="15" r="1" fill="#fff"/></svg></div>
  <h4>All You Need – Full Curriculum</h4>
  <p>This course offers everything you will need to get started as a service dog trainer specialized in medical detection.</p>
  <div class="btn btn-teal">Learn More <svg class="arrow" viewBox="0 0 14 14"><circle cx="7" cy="7" r="7" fill="#fff"/><path d="M5.5 4l3 3-3 3" stroke="var(--teal)" stroke-width="2" fill="none"/></svg></div>
</div>
<div class="course" style="left:446px;top:1641px;height:460px">
  <div class="pic" role="img" aria-label="Dog beside metal scent detection stations" style="background:linear-gradient(170deg,#b7aa97,#8c806e 55%,#514a40)"></div>
  <div class="icon"><svg width="30" height="30" viewBox="0 0 30 30" fill="none" stroke="#fff" stroke-width="2"><path d="M6 22l4-8h10l3-6 3 3-3 3v8M10 14v8M20 14v8"/></svg></div>
  <h4>Service Dog Candidate Selection</h4>
  <p>This course covers everything about dogs. You will have access to our temperament testing protocols, our standards</p>
  <div class="btn btn-teal">Learn More <svg class="arrow" viewBox="0 0 14 14"><circle cx="7" cy="7" r="7" fill="#fff"/><path d="M5.5 4l3 3-3 3" stroke="var(--teal)" stroke-width="2" fill="none"/></svg></div>
</div>
<div class="course" style="left:780px;top:1625px;height:460px">
  <div class="pic" role="img" aria-label="Classroom of trainers watching a presentation" style="background:linear-gradient(160deg,#9fb1a8,#86725e 55%,#5d4a3c)"></div>
  <div class="icon"><svg width="30" height="30" viewBox="0 0 30 30" fill="none" stroke="#fff" stroke-width="2"><rect x="5" y="4" width="20" height="12"/><circle cx="9" cy="21" r="2.5"/><circle cx="15" cy="21" r="2.5"/><circle cx="21" cy="21" r="2.5"/></svg></div>
  <h4>Service Dog Training &amp; Assessments</h4>
  <p>A solid service dog program requires standards, tracking, and testing protocols for the dogs in training.</p>
  <div class="btn btn-teal">Learn More <svg class="arrow" viewBox="0 0 14 14"><circle cx="7" cy="7" r="7" fill="#fff"/><path d="M5.5 4l3 3-3 3" stroke="var(--teal)" stroke-width="2" fill="none"/></svg></div>
</div>

<!-- medical assistance canines -->
<h2 class="abs heading section-title" style="top:2312px">Medical Assistance Canines</h2>

<div class="photo" role="img" aria-label="Trainer working with a black dog indoors" style="left:112px;top:2421px;width:583px;height:341px;background:linear-gradient(100deg,#dedcd6 0%,#b9b3aa 35%,#6b4a38 50%,#cfcac2 75%,#e4e1da 100%)"></div>
<div class="abs" style="left:827px;top:2449px;width:261px;height:297px;border:8px solid var(--blue);border-left:none"></div>
<div class="feature-box" style="left:640px;top:2458px;width:434px;height:278px;background:var(--teal);padding:54px 40px 0 75px">
  <h3>Teaching for Dog Trainers</h3>
  <p>Helping dog trainers improve their skills and learn about service dog training and medical alert dog training.</p>
</div>
<div class="round-icon" style="left:602px;top:2558px;background:var(--blue)"><svg width="38" height="38" viewBox="0 0 38 38" fill="none" stroke="#fff" stroke-width="2"><circle cx="12" cy="9" r="4"/><path d="M12 13v10l-5 9M12 23l5 9M12 16l9 4"/><path d="M22 26l4-6h6l2-4 2 2-2 3v8M26 20v9"/></svg></div>

<div class="photo" role="img" aria-label="Labrador in a vest sniffing scent cans on a tiled floor" style="left:504px;top:2837px;width:584px;height:341px;background:linear-gradient(110deg,#cbc6bd 0%,#a79e90 40%,#e0dcd3 60%,#8d8478 100%)"></div>
<div class="abs" style="left:112px;top:2862px;width:262px;height:300px;border:8px solid var(--teal);border-right:none"></div>
<div class="feature-box" style="left:122px;top:2872px;width:436px;height:280px;background:var(--blue);padding:60px 60px 0 30px;text-align:right">
  <h3 style="text-align:center">Collaborating in Researchprojects</h3>
  <p>Collaborating in research studies in the field of Medical Detection Dogs.</p>
</div>
<div class="round-icon" style="left:522px;top:2970px;background:var(--teal)"><svg width="36" height="36" viewBox="0 0 36 36" fill="none" stroke="#fff" stroke-width="2"><circle cx="18" cy="18" r="6"/><circle cx="18" cy="6" r="3"/><circle cx="18" cy="30" r="3"/><circle cx="6" cy="18" r="3"/><circle cx="30" cy="18" r="3"/><path d="M18 9v3M18 24v3M9 18h3M24 18h3"/></svg></div>

<!-- book -->
<svg class="abs" style="left:0;top:3296px" width="1200" height="570" viewBox="0 0 1200 570"><defs><linearGradient id="bookBand" x1="0" x2="1"><stop offset="0" stop-color="#06a9a0"/><stop offset=".5" stop-color="#109e96"/><stop offset="1" stop-color="#06a9a0"/></linearGradient></defs><path d="M0 110 Q 600 -70 1200 110 L1200 460 Q 600 660 0 460 Z" fill="url(#bookBand)"/></svg>
<h2 class="abs heading book-title">New Book from Helena<br>Marsh Ph.D.!</h2>
<p class="abs book-text">Choosing And Preparing Your Service Dog: A Guide to Confident Public Access Work</p>
<div class="btn btn-blue" style="left:110px;top:3655px;width:140px;height:42px;font-weight:500">Click Here</div>
<div class="photo" role="img" aria-label="Book cover with a golden retriever in a red service vest" style="left:739px;top:3408px;width:207px;height:365px;background:linear-gradient(180deg,#f4f1ec 0%,#efe9e2 40%,#c9a46a 62%,#b12a2e 85%,#9e1f24 100%);box-shadow:6px 6px 14px rgba(0,0,0,.3)"></div>

<!-- blog -->
<h2 class="abs heading section-title" style="top:3940px">Latest Blog</h2>
<article class="post-main">
  <div class="pic" role="img" aria-label="Speaker addressing seated audience in a training hall" style="background:linear-gradient(180deg,#8f8f8a,#4b4d52 60%,#2e3138)"></div>
  <h4>Canine Cognition Testing Seminar</h4>
  <div class="meta">▣ 19 August 2020 &nbsp;|&nbsp; ◯ John Doe</div>
  <p>Learn from scent detection expert Daniel Reyes, how cognition tests can help you improve your results.</p>
</article>
<article class="post-small" style="top:4019px">
  <div class="pic" role="img" aria-label="Black dog in a red service vest" style="background:linear-gradient(140deg,#d8d4cd,#3c3230 60%,#a02a2a)"></div>
  <div class="body"><h5>Lorem ipsum dolor sit onsectetur</h5><div class="meta">▣ 3 May 2018 &nbsp;|&nbsp; ◯ John Doe</div><p>Sed ut perspiciatis unde omnis iste natus error sit voluptatem</p></div>
</article>
<article class="post-small" style="top:4177px">
  <div class="pic" role="img" aria-label="Seminar audience facing a projection screen" style="background:linear-gradient(140deg,#6b7c8c,#8b6d58 60%,#4f3e34)"></div>
  <div class="body"><h5>Lorem ipsum dolor sit onsectetur</h5><div class="meta">▣ Dec 20, 2020 &nbsp;|&nbsp; ◯ John Doe</div><p>Sed ut perspiciatis unde omnis iste natus error sit voluptatem</p></div>
</article>
<article class="post-small" style="top:4334px">
  <div class="pic" role="img" aria-label="Group of trainers posing with their dogs" style="background:linear-gradient(140deg,#a7a39c,#5e5a55 60%,#37342f)"></div>
  <div class="body"><h5>Lorem ipsum dolor sit onsectetur</h5><div class="meta">▣ Dec 19, 2020 &nbsp;|&nbsp; ◯ John Doe</div><p>Sed ut perspiciatis unde omnis iste natus error sit voluptatem</p></div>
</article>

<!-- footer -->
<svg class="abs" style="left:0;top:4570px" width="1200" height="502" viewBox="0 0 1200 502"><path d="M0 100 Q 600 -100 1200 100 L1200 502 L0 502 Z" fill="var(--footer)"/><path d="M0 434 H1200" stroke="#444" stroke-width="1"/></svg>
<div class="foot-h" style="left:110px;top:4700px">Get in touch</div>
<div class="field" style="left:110px;top:4748px;width:236px">First Name</div>
<div class="field" style="left:352px;top:4748px;width:236px">Last Name</div>
<div class="field" style="left:110px;top:4796px;width:236px">Email</div>
<div class="field" style="left:352px;top:4796px;width:236px">phone number</div>
<div class="field" style="left:110px;top:4846px;width:478px;height:68px">Message</div>
<div class="btn btn-teal" style="left:110px;top:4938px;width:98px;height:36px;font-weight:500">Submit</div>

<div class="foot-h" style="left:640px;top:4700px">Quick Links</div>
<ul class="quick">
  <li>›&nbsp; The Center</li><li>›&nbsp; Helping organizations</li><li>›&nbsp; Teaching Trainers</li><li>›&nbsp; Research</li><li>›&nbsp; Contact</li>
</ul>
<div class="foot-h" style="left:640px;top:4916px">Stay Connected :</div>
<span class="social" style="left:840px"></span>
<span class="social" style="left:879px"></span>
<span class="social" style="left:918px"></span>

<div class="foot-h" style="left:851px;top:4700px">Contact Us</div>
<ul class="contact">
  <li><svg viewBox="0 0 14 14"><path d="M7 0a5 5 0 0 0-5 5c0 4 5 9 5 9s5-5 5-9a5 5 0 0 0-5-5z" fill="#fff"/><circle cx="7" cy="5" r="2" fill="var(--footer)"/></svg><span>418 Linden Park Rd Fairview<br>IN 46000</span></li>
  <li><svg viewBox="0 0 14 14"><rect x="3" y="0" width="8" height="14" rx="1.5" fill="#fff"/><rect x="4.5" y="2" width="5" height="8" fill="var(--footer)"/></svg><span>888-888-8888</span></li>
  <li><svg viewBox="0 0 14 14"><rect x="1" y="4" width="12" height="9" rx="1" fill="#fff"/><path d="M3 4V1h8v3" stroke="#fff" stroke-width="1.5" fill="none"/></svg><span>555-014-2278</span></li>
  <li><svg viewBox="0 0 14 14"><rect x="0.7" y="2.7" width="12.6" height="8.6" fill="none" stroke="#fff" stroke-width="1.4"/><path d="M1 3l6 5 6-5" stroke="#fff" stroke-width="1.4" fill="none"/></svg><span>info@brightpathmentor.site</span></li>
</ul>

<p class="copyright">© 2021 brightpathmentor &nbsp;&nbsp;|&nbsp;&nbsp; All Rights Reserved &nbsp;&nbsp;|&nbsp;&nbsp; Terms and Conditions</p>

</body>
</html>
```